business card design for luxurious real estate brand

using the attached logo, i am looking for a 2-sided business card design. the back should be the gold logo on black background. the front needs to include: gold logo, name, phone, email, and website

Industry/Entity Type

real estate

Contact Information for Business Card

logo, name, email, phone, website

Font styles to use
Sans Serif

```html
<!DOCTYPE html>
<html lang="en">
<head>
<meta charset="utf-8">
<title>Casa Ridgeline – Business Card</title>
<link rel="stylesheet" href="https://fonts.googleapis.com/css2?family=Montserrat:wght@400;500;700&display=swap">
<style>
  :root {
    --stage: #1c1c1d;
    --gold: #f5cf14;
    --gold-light: #fbdc22;
    --gold-deep: #e2b90c;
    --gold-ink: #c9a20a;
    --charcoal: #3a3839;
    --charcoal-light: #4d4a4c;
    --charcoal-dark: #262425;
    --soft-white: #e9e7e8;
  }
  * { box-sizing: border-box; margin: 0; padding: 0; }
  html, body {
    width: 1200px; height: 1200px; overflow: hidden;
    background: var(--stage);
    font-family: "Montserrat", sans-serif;
  }
  .canvas {
    width: 1200px; height: 1200px;
    display: flex; flex-direction: column; align-items: center; justify-content: center;
    gap: 44px;
  }
  .card {
    width: 900px; height: 514px;
    position: relative;
    border-radius: 3px;
  }
  .card--back {
    background: linear-gradient(135deg, var(--gold-light) 0%, var(--gold) 55%, var(--gold-deep) 100%);
    display: flex; align-items: center; justify-content: center;
  }
  .card--front {
    background: radial-gradient(ellipse at 65% 35%, var(--charcoal-light) 0%, var(--charcoal) 45%, var(--charcoal-dark) 100%);
  }
  .brand {
    display: flex; align-items: center; gap: 18px;
    font-weight: 500;
    letter-spacing: 0.32em;
    text-transform: uppercase;
  }
  .brand__mark { width: 22px; height: 22px; }
  .card--back .brand { color: var(--gold-ink); font-size: 34px; }
  .card--back .brand__mark { background: var(--gold-ink); }
  .card--front .brand {
    position: absolute; left: 90px; top: 120px;
    color: var(--gold); font-size: 28px;
  }
  .card--front .brand__mark { background: var(--gold); width: 18px; height: 18px; }
  .contact {
    position: absolute; left: 470px; top: 270px; width: 360px;
  }
  .contact__name {
    color: var(--gold); font-weight: 700; font-size: 34px; line-height: 1.1;
  }
  .contact__role {
    color: var(--soft-white); font-weight: 400; font-size: 18px; margin-top: 6px;
  }
  .contact__rule {
    height: 2px; background: var(--gold); margin: 14px 0 16px; width: 100%;
  }
  .contact__list { list-style: none; }
  .contact__item {
    display: flex; align-items: center; gap: 12px;
    color: var(--soft-white); font-size: 17px; line-height: 1.75;
  }
  .contact__icon { width: 16px; height: 16px; fill: var(--gold); flex: none; }
</style>
</head>
<body>
<main class="canvas">
  <section class="card card--back" aria-label="Card back">
    <div class="brand"><span class="brand__mark"></span>Casa Ridgeline</div>
  </section>

  <section class="card card--front" aria-label="Card front">
    <div class="brand"><span class="brand__mark"></span>Casa Ridgeline</div>
    <div class="contact">
      <p class="contact__name">Marlow Venn</p>
      <p class="contact__role">Founder &amp; Director</p>
      <div class="contact__rule"></div>
      <ul class="contact__list">
        <li class="contact__item">
          <svg class="contact__icon" viewBox="0 0 24 24" aria-hidden="true"><path d="M6.6 10.8a15.1 15.1 0 0 0 6.6 6.6l2.2-2.2c.3-.3.7-.4 1-.2 1.1.4 2.3.6 3.6.6.6 0 1 .4 1 1V20c0 .6-.4 1-1 1A17 17 0 0 1 3 4c0-.6.4-1 1-1h3.5c.6 0 1 .4 1 1 0 1.3.2 2.5.6 3.6.1.3 0 .7-.2 1z"/></svg>
          (405)-555-0147
        </li>
        <li class="contact__item">
          <svg class="contact__icon" viewBox="0 0 24 24" aria-hidden="true"><path d="M2 5h20v14H2zm2 2v.4l8 5 8-5V7l-8 5z"/></svg>
          marlow@casaridgeline.com
        </li>
        <li class="contact__item">
          <svg class="contact__icon" viewBox="0 0 24 24" aria-hidden="true"><path d="M12 2a10 10 0 1 0 0 20 10 10 0 0 0 0-20zm6.9 6h-3a15 15 0 0 0-1.3-3.9A8 8 0 0 1 18.9 8zM12 4c.8 1.1 1.5 2.5 1.9 4h-3.8c.4-1.5 1.1-2.9 1.9-4zM4.3 14a8 8 0 0 1 0-4h3.4a16 16 0 0 0 0 4zm.8 2h3a15 15 0 0 0 1.3 3.9A8 8 0 0 1 5.1 16zm3-8h-3a8 8 0 0 1 4.3-3.9A15 15 0 0 0 8.1 8zM12 20c-.8-1.1-1.5-2.5-1.9-4h3.8c-.4 1.5-1.1 2.9-1.9 4zm2.3-6H9.7a14 14 0 0 1 0-4h4.6a14 14 0 0 1 0 4zm.3 5.9a15 15 0 0 0 1.3-3.9h3a8 8 0 0 1-4.3 3.9zm1.7-5.9a16 16 0 0 0 0-4h3.4a8 8 0 0 1 0 4z"/></svg>
          www.casaridgeline.com
        </li>
      </ul>
    </div>
  </section>
</main>
</body>
</html>
```